Website design and coding for new consultancy company

I need to have a full website designed for a new consultancy business I'm trying to establish. It's called Brightpath consult. I need an English version to begin with, and then there should be a Danish version as well, but I'll translate that myself. Just be aware that I need two language versions. The consultancy field that I'm targeting is Leadership - and specialist development. I offer to facilitate corporate academies for global companies as well as specific workshops within leadership- or team development, strategy sessions, personal coaching and facilitation of D&I (Diversity and inclusion) workshops. BTW my logo is not in high resolution - I need that as well.

Target Market(s)

Larger companies that has a need for developing their inhouse leadership capabilities or that wants to develop their specialists to take on more responsibility.

Industry/Entity Type

Consultancy business

Coding

Number of Pages Required

5+ page

Requirements
Must have
• Introduction site with a catch phrase. Book a meeting. Services that's beeing offered. Blog site with white papers etc. Language toggle (Danish/English). Cases/testimonials. About site. Contact site.

```html
<!DOCTYPE html>
<html lang="en">
<head>
<meta charset="utf-8">
<title>Brightpath Consult</title>
<link href="https://fonts.googleapis.com/css2?family=Oswald:wght@400;500;600&family=Lato:wght@400;700&display=swap" rel="stylesheet">
<style>
:root{
  --ink:#111111;
  --text:#2a2a2a;
  --brand:#1f7fc9;
  --brand-deep:#0d4ea6;
  --pale:#eef7fd;
  --white:#ffffff;
  --footer:#2185cc;
  --hero-a:#3b4a57;
  --hero-b:#6b5a48;
}
*{box-sizing:border-box;margin:0;padding:0}
html,body{width:1200px;height:2445px;overflow:hidden}
body{font-family:'Lato',sans-serif;color:var(--text);background:var(--white);position:relative}
.display{font-family:'Oswald',sans-serif;text-transform:uppercase}
a{color:inherit}

/* header */
.site-header{position:absolute;left:0;top:0;width:1200px;height:94px;background:var(--white)}
.brand-name{position:absolute;left:112px;top:18px;font-family:'Oswald',sans-serif;font-weight:600;font-size:38px;color:var(--ink);letter-spacing:.5px;line-height:1}
.main-nav{position:absolute;left:0;top:35px;font-family:'Oswald',sans-serif;font-size:16px;color:var(--ink);text-transform:uppercase}
.main-nav span{position:absolute;white-space:nowrap}
.main-nav .active{color:var(--brand);text-decoration:underline}
.btn-contact{position:absolute;left:907px;top:28px;width:112px;height:39px;background:var(--brand);color:var(--white);font-family:'Oswald',sans-serif;font-size:16px;display:flex;align-items:center;justify-content:center;border-radius:2px}
.lang{position:absolute;left:1048px;top:38px;font-family:'Oswald',sans-serif;font-size:15px;display:flex;gap:5px;align-items:center}

/* hero */
.hero{position:absolute;left:0;top:94px;width:1200px;height:502px;background:linear-gradient(120deg,#4a5560 0%,var(--hero-a) 35%,#2c3640 60%,var(--hero-b) 100%)}
.hero-photo{position:absolute;inset:0;background:radial-gradient(ellipse at 30% 60%,rgba(150,120,90,.35),transparent 60%),radial-gradient(ellipse at 80% 70%,rgba(180,140,100,.3),transparent 55%)}
.hero-shade{position:absolute;inset:0;background:rgba(20,28,36,.45)}
.hero-copy{position:absolute;left:0;width:1200px;text-align:center;color:var(--white)}
.hero-kicker{top:116px;font-family:'Lato',sans-serif;font-size:25px;font-weight:700;letter-spacing:.3px}
.hero-title{top:160px;font-family:'Oswald',sans-serif;font-weight:500;font-size:56px;letter-spacing:.5px}
.hero-lede{top:240px;font-size:19px;line-height:29px;font-weight:700;padding:0 240px}
.btn-start{position:absolute;left:535px;top:311px;width:131px;height:47px;background:var(--white);color:var(--brand-deep);font-family:'Oswald',sans-serif;font-size:16px;display:flex;align-items:center;justify-content:center;border-radius:2px}
.hero-arrow{position:absolute;top:224px;width:30px;height:30px;border-radius:50%;display:flex;align-items:center;justify-content:center}
.hero-arrow.prev{left:37px;background:rgba(255,255,255,.35)}
.hero-arrow.next{left:1131px;background:var(--white)}
.scroll-down{position:absolute;left:581px;top:578px;width:38px;height:38px;border-radius:50%;background:var(--brand);border:3px solid var(--white);display:flex;align-items:center;justify-content:center;z-index:2}

/* about */
.about{position:absolute;left:0;top:596px;width:1200px;height:659px}
.section-title{font-family:'Oswald',sans-serif;font-weight:500;font-size:40px;color:var(--ink);text-transform:uppercase;line-height:1}
.section-title em{font-style:normal;color:var(--brand-deep)}
.about .section-title{position:absolute;left:108px;top:92px}
.rule{position:absolute;height:3px;width:74px;background:var(--brand-deep)}
.about .rule{left:111px;top:153px}
.about-text{position:absolute;left:111px;top:172px;width:452px;font-size:15.5px;line-height:29px;text-align:justify}
.about-text p+p{margin-top:29px}
.btn-read{position:absolute;left:111px;top:478px;width:142px;height:51px;background:var(--brand);color:var(--white);font-family:'Oswald',sans-serif;font-size:17px;display:flex;align-items:center;justify-content:center;border-radius:4px}
.portrait-frame{position:absolute;left:573px;top:155px;width:607px;height:396px;background:var(--brand)}
.portrait{position:absolute;left:662px;top:52px;width:427px;height:482px;background:linear-gradient(180deg,#f4f6f8 0%,#c9d6e2 55%,#8ea8c0 100%)}

/* services */
.services{position:absolute;left:0;top:1255px;width:1200px;height:785px;background:var(--pale)}
.services .section-title{position:absolute;left:0;width:1200px;text-align:center;top:65px}
.services .rule{left:563px;top:128px}
.services-lede{position:absolute;left:0;width:1200px;top:152px;text-align:center;font-size:17px;line-height:29px;color:var(--ink)}
.card{position:absolute;top:243px;background:var(--white);border:1px solid #d9dde1}
.card.featured{border:none;box-shadow:0 6px 20px rgba(0,0,0,.08);top:243px}
.card-head{height:57px;padding:18px 18px 0;font-family:'Oswald',sans-serif;font-size:20px;color:var(--ink);text-transform:uppercase}
.card.featured .card-head{color:var(--brand-deep);font-weight:500}
.card-img{height:221px}
.card-body{padding:15px 13px 0;font-size:14.5px;line-height:27.5px;color:var(--ink)}
.card-link{display:block;margin-top:6px;font-family:'Oswald',sans-serif;font-size:14px;text-decoration:underline;color:var(--ink)}
.card.featured .card-link{color:var(--brand-deep)}
.svc-arrow{position:absolute;top:457px;width:35px;height:35px;border-radius:50%;background:#777b80;display:flex;align-items:center;justify-content:center}
.svc-arrow.next{background:#a7abb0}

/* footer */
.site-footer{position:absolute;left:0;top:2040px;width:1200px;height:405px;background:var(--footer);color:var(--white)}
.footer-brand{position:absolute;left:113px;top:77px;width:261px;height:87px;background:var(--white);display:flex;align-items:center;justify-content:center;font-family:'Oswald',sans-serif;font-weight:600;font-size:36px;color:var(--ink)}
.socials{position:absolute;left:111px;top:221px;display:flex;gap:26px}
.socials span{width:32px;height:32px;border-radius:50%;background:var(--white)}
.f-col{position:absolute;top:78px}
.f-col h3{font-family:'Oswald',sans-serif;font-weight:400;font-size:21px;text-transform:uppercase;margin-bottom:12px}
.f-col li{list-style:none;font-size:16px;height:34px;display:flex;align-items:center;gap:9px}
.contact-row{display:flex;gap:12px;font-size:15.5px;line-height:23.5px;margin-bottom:17px}
.contact-row i{flex:none;width:32px;height:32px;border-radius:50%;background:var(--white);display:flex;align-items:center;justify-content:center}
.footer-rule{position:absolute;left:111px;top:323px;width:978px;height:1px;background:rgba(255,255,255,.6)}
.copyright{position:absolute;left:0;width:1200px;top:358px;text-align:center;font-size:16px;font-weight:700}
</style>
</head>
<body>

<header class="site-header">
  <div class="brand-name">BRIGHTPATH</div>
  <nav class="main-nav">
    <span class="active" style="left:420px">Home</span>
    <span style="left:507px">About</span>
    <span style="left:599px">Services</span>
    <span style="left:712px">Blog</span>
    <span style="left:803px">Approach</span>
  </nav>
  <div class="btn-contact">CONTACT US</div>
  <div class="lang">EN
    <svg width="20" height="20" viewBox="0 0 20 20" fill="none" stroke="#111" stroke-width="1.3"><circle cx="10" cy="10" r="8.5"/><ellipse cx="10" cy="10" rx="3.8" ry="8.5"/><path d="M1.5 10h17M3 5.5h14M3 14.5h14"/></svg>
  </div>
</header>

<section class="hero">
  <div class="hero-photo" role="img" aria-label="Photo of a diverse team collaborating around a laptop in an office"></div>
  <div class="hero-shade"></div>
  <div class="hero-copy hero-kicker">WELCOME TO BRIGHTPATH</div>
  <h1 class="hero-copy hero-title">EMPOWERING LEADERS. ENABLING GROWTH.</h1>
  <p class="hero-copy hero-lede">Brightpath Consult supports global companies in developing leaders, specialists, and inclusive workplaces.</p>
  <div class="btn-start">GET STARTED</div>
  <div class="hero-arrow prev"><svg width="12" height="12" viewBox="0 0 12 12"><path d="M8 1L3 6l5 5" stroke="#fff" stroke-width="2" fill="none"/></svg></div>
  <div class="hero-arrow next"><svg width="12" height="12" viewBox="0 0 12 12"><path d="M4 1l5 5-5 5" stroke="#111" stroke-width="2" fill="none"/></svg></div>
</section>
<div class="scroll-down"><svg width="14" height="16" viewBox="0 0 14 16"><path d="M7 1v13M1.5 8.5L7 14l5.5-5.5" stroke="#fff" stroke-width="2" fill="none"/></svg></div>

<section class="about">
  <h2 class="section-title">About <em>Brightpath Consult</em></h2>
  <div class="rule"></div>
  <div class="about-text">
    <p>At Brightpath Consult, we specialize in leadership and specialist development for international organizations. With experience in facilitating corporate academies, leading workshops, and guiding leadership teams, we combine global perspective with practical tools that create real change.</p>
    <p>Excepteur sint occaecat cupidatat non proident, sunt in culpa qui officia deserunt mollit anim id est laborum sunt in culpa qui ooccaecat cupidatat non proident, sunt in culpa qui officia deserunt mollitfficia deserunt mollit anim id est laborum.</p>
  </div>
  <div class="btn-read">READ MORE</div>
  <div class="portrait-frame"></div>
  <div class="portrait" role="img" aria-label="Portrait photo of the consultancy founder in a suit"></div>
</section>

<section class="services">
  <h2 class="section-title">Our <em>Services</em></h2>
  <div class="rule"></div>
  <p class="services-lede">With experience in facilitating corporate academies, leading workshops, and guiding leadership teams,<br>we combine global perspective with practical tools that create real change.</p>

  <div class="svc-arrow prev" style="left:34px"><svg width="18" height="14" viewBox="0 0 18 14"><path d="M17 7H2M7 1.5L1.5 7 7 12.5" stroke="#fff" stroke-width="2.4" fill="none"/></svg></div>
  <div class="svc-arrow next" style="left:1131px"><svg width="18" height="14" viewBox="0 0 18 14"><path d="M1 7h15M11 1.5L16.5 7 11 12.5" stroke="#fff" stroke-width="2.4" fill="none"/></svg></div>

  <article class="card" style="left:111px;width:297px">
    <h3 class="card-head">Team Development</h3>
    <div class="card-img" role="img" aria-label="Photo of two colleagues working together at a laptop" style="background:linear-gradient(135deg,#d98a2b,#b0652a 50%,#5a4a3a)"></div>
    <div class="card-body">Lorem ipsum dolor sit amet, conse ctetur adipiscing elit, sed do eiusmod unt eiusmod tempor incididunt ut labore ut labore et dolore magna aliqua.<a class="card-link">Read More</a></div>
  </article>
  <article class="card featured" style="left:435px;width:331px">
    <h3 class="card-head">Strategy Sessions</h3>
    <div class="card-img" role="img" aria-label="Photo of a woman arranging notes on a planning board" style="background:linear-gradient(135deg,#3d4650,#7e9aa3 50%,#d9dcd6)"></div>
    <div class="card-body" style="padding-left:20px">Lorem ipsum dolor sit amet, conse ctetur adipis cing elit, sed do eiusmod unt eiusmod didunt ut labore tempor incididunt ut labore et dolore magna aliqua.<a class="card-link">Read More</a></div>
  </article>
  <article class="card" style="left:792px;width:297px">
    <h3 class="card-head">Personal Coaching</h3>
    <div class="card-img" role="img" aria-label="Photo of a coaching conversation between two people at a desk" style="background:linear-gradient(135deg,#6b5a4a,#cfc6bb 50%,#3a3f45)"></div>
    <div class="card-body">Lorem ipsum dolor sit amet, conse ctetur adipiscing elit, sed do eiusmod unt eiusmod tempor incididunt ut labore ut labore et dolore magna aliqua.<a class="card-link">Read More</a></div>
  </article>
</section>

<footer class="site-footer">
  <div class="footer-brand">BRIGHTPATH</div>
  <div class="socials"><span></span><span></span><span></span><span></span></div>

  <div class="f-col" style="left:447px">
    <h3>Quick Links</h3>
    <ul>
      <li><svg width="14" height="12" viewBox="0 0 14 12"><path d="M1 6h11M7.5 1.5L12 6l-4.5 4.5" stroke="#fff" stroke-width="2.2" fill="none"/></svg>Home</li>
      <li><svg width="14" height="12" viewBox="0 0 14 12"><path d="M1 6h11M7.5 1.5L12 6l-4.5 4.5" stroke="#fff" stroke-width="2.2" fill="none"/></svg>About</li>
      <li><svg width="14" height="12" viewBox="0 0 14 12"><path d="M1 6h11M7.5 1.5L12 6l-4.5 4.5" stroke="#fff" stroke-width="2.2" fill="none"/></svg>Services</li>
      <li><svg width="14" height="12" viewBox="0 0 14 12"><path d="M1 6h11M7.5 1.5L12 6l-4.5 4.5" stroke="#fff" stroke-width="2.2" fill="none"/></svg>Approach</li>
      <li><svg width="14" height="12" viewBox="0 0 14 12"><path d="M1 6h11M7.5 1.5L12 6l-4.5 4.5" stroke="#fff" stroke-width="2.2" fill="none"/></svg>Contact Us</li>
    </ul>
  </div>

  <div class="f-col" style="left:660px">
    <h3>Help Links</h3>
    <ul>
      <li><svg width="14" height="12" viewBox="0 0 14 12"><path d="M1 6h11M7.5 1.5L12 6l-4.5 4.5" stroke="#fff" stroke-width="2.2" fill="none"/></svg>FAQ</li>
      <li><svg width="14" height="12" viewBox="0 0 14 12"><path d="M1 6h11M7.5 1.5L12 6l-4.5 4.5" stroke="#fff" stroke-width="2.2" fill="none"/></svg>Terms of use</li>
      <li><svg width="14" height="12" viewBox="0 0 14 12"><path d="M1 6h11M7.5 1.5L12 6l-4.5 4.5" stroke="#fff" stroke-width="2.2" fill="none"/></svg>Privacy Policy</li>
      <li><svg width="14" height="12" viewBox="0 0 14 12"><path d="M1 6h11M7.5 1.5L12 6l-4.5 4.5" stroke="#fff" stroke-width="2.2" fill="none"/></svg>Support Links</li>
      <li><svg width="14" height="12" viewBox="0 0 14 12"><path d="M1 6h11M7.5 1.5L12 6l-4.5 4.5" stroke="#fff" stroke-width="2.2" fill="none"/></svg>Conditions</li>
    </ul>
  </div>

  <div class="f-col" style="left:867px">
    <h3>Contact Us</h3>
    <div class="contact-row"><i><svg width="14" height="18" viewBox="0 0 14 18"><path d="M7 1a6 6 0 0 0-6 6c0 4.5 6 10 6 10s6-5.5 6-10a6 6 0 0 0-6-6z" fill="#1f7fc9"/><circle cx="7" cy="7" r="2.2" fill="#fff"/></svg></i><span>Brightpath consult<br>United States</span></div>
    <div class="contact-row" style="align-items:center"><i><svg width="16" height="16" viewBox="0 0 16 16"><path d="M3 1.5l2.5 0 1.2 3.2-1.6 1.2a8 8 0 0 0 5 5l1.2-1.6 3.2 1.2v2.5c0 .8-.7 1.5-1.5 1.5C7 14.5 1.5 9 1.5 3c0-.8.7-1.5 1.5-1.5z" fill="#1f7fc9"/></svg></i><span>+1 555 010 0199</span></div>
    <div class="contact-row" style="align-items:center"><i><svg width="16" height="12" viewBox="0 0 16 12"><rect x="0.5" y="0.5" width="15" height="11" rx="1.5" fill="#1f7fc9"/><path d="M1 1.5l7 5 7-5" stroke="#fff" stroke-width="1.3" fill="none"/></svg></i><span>info@brightpathconsult.com</span></div>
  </div>

  <div class="footer-rule"></div>
  <p class="copyright">Copyrights@2025.Brightpath consult.All Rights Reserved</p>
</footer>

</body>
</html>
```